Stationary for Beauty and Spa School

Create a business card, letterhead and envelopes (primarily #10 envelope with and without window and catalog envelope) for a beauty and wellness school in Miami, Fl. We offer 8 different programs of study and need an eye catching look. Looking for a combination of modern yet sophisticated. Nothing corporate or business looking. Would like to have a look and feel that is similar (or incorporates aspects) of a new website we will be launching in the next 30 days (screen shot attached.)

The final design should communicate style and elegance in a down to earth and friendly way. We strive to provide our students with quality education, friendly and amicable staff and experienced instructors.
Updates

Hello. FYI, in order to print an aesthetically appealing business card, we would like to print them (the business cards) using silk printing method, with spot UV coating (on some elements, maybe the logo, or depending on the design) and die cuts. Please think of this when preparing your design.

Only 1 day left, please submit your designs for selection. Thanks

Target Market(s)

Adults 18-49 years who are mostly interested in beauty and fashion. Need a youthful & modern look, yet sophisticated and elegant.

Industry/Entity Type

School

Colors
e34197
6b449b
add136
f79021

Requirements
Must have
• Similar look and feel as website (see attached screen shot)
Same look and feel of website (see attached screenshot)
Logo
Address: 5216 SW 3rd Avenue. Miami, Fl 33155
Telephone: 305-514-9382
Fax: 786-420-5163
website/url: www.luminora.edu
incorporate Photo of blonde model (attached)
Nice to have
• Tag line: "Beautify your future." Also, maybe two-sided business card. Would be nice if we could mention our programs (maybe in the back of the card). Below are the program offerings (names cannot be changed but order is irrelevant)... Cosmetology, Barber, Spa Therapy, Massage Therapy, Makeup Artistry, Skin Care, Manicure, Pedicure & Nail Extensions, Full Specialist.

A design with text plus a beautiful photo of a model is appealing. Attached to the files is a sample of a cover for a student handbook we have created. You should use the photo of the blonde model (attached) in your design. The original (quality) version of this stock photograph has been uploaded.

Also would be nice to request clients to follow us on facebook and instagram by including the icons.
Should not have
• A corporate or business look. We are a vocational school teaching beauty and spa programs and we like our advertising to have a look that resembles the industry. We do not want a very serious look or snobby feel.

```html
<!DOCTYPE html>
<html lang="en">
<head>
<meta charset="utf-8">
<title>Luminora School of Beauty – Business Card</title>
<link rel="stylesheet" href="https://fonts.googleapis.com/css2?family=Arimo:wght@400;700&display=swap">
<style>
  :root {
    --green: #add136;
    --purple: #6b449b;
    --magenta: #e34197;
    --orange: #f79021;
    --ink: #1c1c1c;
    --card-black: #161616;
    --logo-grey: #6a6a6a;
    --white: #ffffff;
    --page: #ecebe9;
    --social: #1e8fd6;
  }
  * { box-sizing: border-box; margin: 0; padding: 0; }
  html, body { width: 1200px; height: 716px; overflow: hidden; }
  body {
    background: var(--page);
    font-family: "Arimo", Arial, sans-serif;
    position: relative;
  }
  .card {
    position: absolute;
    top: 210px;
    width: 520px;
    height: 297px;
    border-radius: 18px;
    overflow: hidden;
    box-shadow: 0 6px 18px rgba(0,0,0,0.18);
  }
  .card--front { left: 60px; background: var(--white); }
  .card--back { left: 620px; background: var(--card-black); color: var(--white); }

  .color-band { position: absolute; display: flex; height: 7px; }
  .color-band span { flex: 1; }
  .color-band .c1 { background: var(--green); }
  .color-band .c2 { background: var(--purple); }
  .color-band .c3 { background: var(--magenta); }
  .color-band .c4 { background: var(--orange); }
  .card--front .color-band { left: 0; right: 0; bottom: 0; }
  .card--back .color-band { left: 38%; right: 0; top: 0; }

  /* front */
  .model-photo {
    position: absolute; left: 0; top: 0; bottom: 7px; width: 330px;
    background:
      linear-gradient(90deg, rgba(255,255,255,0) 55%, var(--white) 100%),
      linear-gradient(160deg, #e9dcc4 0%, #d9b9a0 30%, #f1e6d6 55%, #f6f2ec 80%);
  }
  .brand {
    position: absolute; left: 300px; top: 95px; color: var(--ink); font-weight: 700;
  }
  .brand__name { font-size: 42px; letter-spacing: 0.5px; line-height: 1; }
  .brand__sub { font-size: 11px; letter-spacing: 0.8px; text-transform: uppercase; margin-top: 4px; padding-left: 40px; }
  .tagline { position: absolute; left: 300px; top: 175px; font-size: 19px; line-height: 1.15; text-transform: uppercase; }
  .tagline__first { letter-spacing: 6px; }
  .tagline .g { color: var(--green); }
  .tagline .m { color: var(--magenta); }
  .tagline .o { color: var(--orange); }

  /* back */
  .card--back .brand { left: 30px; top: 38px; color: var(--logo-grey); }
  .card--back .brand__sub { color: var(--logo-grey); }
  .person { position: absolute; left: 268px; top: 100px; }
  .person__name { font-size: 23px; text-transform: uppercase; letter-spacing: 0.3px; }
  .person__title { font-size: 14px; margin-top: 3px; }
  .rule { position: absolute; left: 268px; top: 160px; width: 230px; height: 1px; background: var(--magenta); }
  .contact { position: absolute; left: 268px; top: 172px; font-size: 14px; line-height: 18px; }
  .contact__row { display: flex; align-items: center; gap: 8px; }
  .contact__row svg { width: 13px; height: 13px; fill: var(--magenta); }
  .contact__address { margin-top: 6px; }
  .contact__web { margin-top: 6px; font-weight: 700; font-size: 15px; }
  .social { position: absolute; left: 30px; top: 218px; display: flex; align-items: center; gap: 6px; font-size: 14px; }
  .social__dot { width: 18px; height: 18px; border-radius: 50%; background: var(--social); }
  .social__handle { margin-left: 8px; }
</style>
</head>
<body>
  <section class="card card--front">
    <div class="model-photo" role="img" aria-label="Photo of a blonde model with bold makeup"></div>
    <div class="brand">
      <div class="brand__name">Luminora</div>
      <div class="brand__sub">School of Beauty</div>
    </div>
    <p class="tagline">
      <span class="tagline__first"><span class="g">Beau</span><span class="m">tify</span></span><br>
      <span class="o">Your </span><span class="m">Future.</span>
    </p>
    <div class="color-band"><span class="c1"></span><span class="c2"></span><span class="c3"></span><span class="c4"></span></div>
  </section>

  <section class="card card--back">
    <div class="color-band"><span class="c1"></span><span class="c2"></span><span class="c3"></span><span class="c4"></span></div>
    <div class="brand">
      <div class="brand__name">Luminora</div>
      <div class="brand__sub">School of Beauty</div>
    </div>
    <div class="person">
      <div class="person__name">Dana Whitfield</div>
      <div class="person__title">Director</div>
    </div>
    <div class="rule"></div>
    <div class="contact">
      <div class="contact__row">
        <svg viewBox="0 0 24 24" aria-hidden="true"><path d="M6.6 10.8a15 15 0 0 0 6.6 6.6l2.2-2.2c.3-.3.7-.4 1-.2 1.1.4 2.3.6 3.6.6.6 0 1 .4 1 1V20c0 .6-.4 1-1 1A17 17 0 0 1 3 4c0-.6.4-1 1-1h3.5c.6 0 1 .4 1 1 0 1.2.2 2.4.6 3.6.1.3 0 .7-.2 1z"/></svg>
        <span>305-514-9382</span>
      </div>
      <div class="contact__row">
        <svg viewBox="0 0 24 24" aria-hidden="true"><path d="M7 3h9v5H7zM4 9h16a2 2 0 0 1 2 2v7h-4v3H6v-3H2v-7a2 2 0 0 1 2-2zm4 7v3h8v-3z"/></svg>
        <span>786-420-5163</span>
      </div>
      <div class="contact__address">5216 SW 3rd Avenue<br>Miami, Fl 33155</div>
      <div class="contact__web">www.luminora.edu</div>
    </div>
    <div class="social">
      <span class="social__dot"></span>
      <span class="social__dot"></span>
      <span class="social__handle">/luminora.edu</span>
    </div>
  </section>
</body>
</html>
```